A5 Magazine Cover Design

I need a front cover designing for a new community magazine called BELVOR. BELVOR will be listing local buisnesses and local interest articles for the residents in my area. I need the look to be clean but inviting.

I will consider any colour combination as long as its not too bright.

```html
<!DOCTYPE html>
<html lang="en">
<head>
<meta charset="utf-8">
<title>BELVOR – Community Magazine Cover</title>
<link href="https://fonts.googleapis.com/css2?family=Great+Vibes&family=Arimo:wght@400&display=swap" rel="stylesheet">
<style>
  :root {
    --backdrop: #ecebe8;
    --sky-top: #7ab8e6;
    --sky-bottom: #2a7dc6;
    --orange: #f7860f;
    --orange-deep: #ef6f06;
    --lime: #c9e41a;
    --leaf: #3f9a1e;
    --white: #ffffff;
    --photo-light: #f3f1ea;
    --photo-warm: #f2c21c;
    --photo-grey: #c9c6bd;
  }
  * { margin: 0; padding: 0; box-sizing: border-box; }
  html, body {
    width: 1200px;
    height: 1200px;
    overflow: hidden;
    background: var(--backdrop);
  }
  .cover {
    position: absolute;
    left: 248px;
    top: 100px;
    width: 704px;
    height: 1000px;
    overflow: hidden;
    box-shadow: 0 6px 24px rgba(0,0,0,0.18);
  }
  .cover-art {
    position: absolute;
    inset: 0;
    width: 100%;
    height: 100%;
    display: block;
  }
  .masthead {
    position: absolute;
    left: 48px;
    top: 545px;
    font-family: "Great Vibes", cursive;
    font-size: 150px;
    line-height: 1;
    color: var(--lime);
    font-weight: 400;
  }
  .features {
    position: absolute;
    left: 262px;
    top: 790px;
    list-style: none;
    font-family: "Arimo", Arial, sans-serif;
    font-size: 29px;
    color: var(--white);
    line-height: 40px;
  }
  .features li {
    position: relative;
    padding-left: 38px;
  }
  .features li::before {
    content: "";
    position: absolute;
    left: 0;
    top: 11px;
    border-left: 20px solid var(--lime);
    border-top: 9px solid transparent;
    border-bottom: 9px solid transparent;
  }
</style>
</head>
<body>
  <main class="cover">
    <svg class="cover-art" viewBox="0 0 420 597" preserveAspectRatio="none" xmlns="http://www.w3.org/2000/svg">
      <defs>
        <linearGradient id="sky" x1="0" y1="0" x2="0" y2="1">
          <stop offset="0" stop-color="var(--sky-top)"/>
          <stop offset="1" stop-color="var(--sky-bottom)"/>
        </linearGradient>
        <linearGradient id="photoTone" x1="0" y1="0" x2="1" y2="0.6">
          <stop offset="0" stop-color="var(--photo-warm)"/>
          <stop offset="0.35" stop-color="var(--photo-light)"/>
          <stop offset="1" stop-color="var(--photo-grey)"/>
        </linearGradient>
        <linearGradient id="leafSweep" x1="1" y1="0" x2="0" y2="1">
          <stop offset="0" stop-color="var(--lime)"/>
          <stop offset="1" stop-color="var(--leaf)"/>
        </linearGradient>
        <linearGradient id="leafBase" x1="0" y1="0" x2="1" y2="1">
          <stop offset="0" stop-color="var(--lime)"/>
          <stop offset="1" stop-color="var(--leaf)"/>
        </linearGradient>
      </defs>

      <rect class="cover-ground" width="420" height="597" fill="url(#sky)"/>

      <path class="cover-photo" role="img" aria-label="Photograph of a property sale agreement under a magnifying glass on a yellow folder"
            d="M0 0 H420 V200 C360 250 280 275 200 272 C110 268 40 230 0 185 Z" fill="url(#photoTone)"/>

      <path class="band-orange"
            d="M0 185 C40 230 110 268 200 272 C280 275 360 250 420 200 V238 C360 285 270 310 190 306 C110 302 40 262 0 226 Z"
            fill="var(--orange)"/>
      <path class="band-rule" d="M0 226 C40 262 110 302 190 306 C270 310 360 285 420 238"
            fill="none" stroke="var(--white)" stroke-width="3"/>
      <path class="sweep-leaf"
            d="M420 120 C385 195 300 250 175 268 C300 238 385 190 420 150 Z" fill="url(#leafSweep)"/>

      <path class="base-leaf" d="M0 515 C90 540 180 570 250 597 H236 C170 578 85 556 0 543 Z" fill="url(#leafBase)"/>
      <path class="base-rule" d="M0 543 C85 556 170 578 236 597" fill="none" stroke="var(--white)" stroke-width="1.5"/>
      <path class="base-orange" d="M0 545 C85 558 170 580 232 597 H0 Z" fill="var(--orange-deep)"/>
    </svg>

    <h1 class="masthead">Belvor</h1>

    <ul class="features">
      <li>Searches,</li>
      <li>Reviews</li>
      <li>and Recommends Locally</li>
    </ul>
  </main>
</body>
</html>
```